Webdesign für Bilderbücher für Kinder
Zielgruppe
Wir sind ein Verlag für zweisprachige Bilderbücher für Kinder im Alter von 2-8 Jahren. Wir suchen ein Design für eine mit SHOPIFY neu zu erstellende Website, über die die Bücher verkauft werden sollen.
Der Verlag ist das deutsche Imprint eines internationalen Autoren (zur Orientierung siehe www.karlwendtbooks.com oder kurzlnk.net/karlwendt).
Da das Thema sehr bunt ist und mit der Sprachen-Niche noch nicht prominent besetzt ist, wollen wir hier bewusst NICHT so viele Vorgaben machen, was das Design angeht.
Aufgabenstellung
Logo und Beispiele aus bestehenden Büchern sind als Attachments angehängt.
Beispielseiten zur Orientierung, die uns gefallen, sind die folgenden:
https://www.karlwendtbooks.com/
https://www.edition-morapo.com/
Ein gutes Design hat der Honigtau Verlag
https://www.honigtauverlag.de/
oder der Seraph Verlag
https://shop.seraph-verlag.de/

```html
<!DOCTYPE html>
<html lang="de">
<head>
<meta charset="utf-8">
<title>Bunte Welt Verlag – Webdesign</title>
<link rel="stylesheet" href="https://fonts.googleapis.com/css2?family=Roboto:wght@300;400;500;700&family=Source+Serif+4:wght@400;600&display=swap">
<style>
:root{
  --backdrop:#1e1e1e;
  --paper:#f2f2f2;
  --sand:#e9e5df;
  --blue:#4a6f8b;
  --blue-dark:#3f6580;
  --ink:#4d6d86;
  --muted:#7d8f9c;
  --line:#d3d3d3;
}
*{box-sizing:border-box;margin:0;padding:0}
html,body{width:1200px;height:1186px;overflow:hidden;background:var(--backdrop)}
body{font-family:"Roboto",Arial,sans-serif;color:var(--ink)}
.stage{position:absolute;left:0;top:0;width:1932px;height:1910px;transform:scale(.62112);transform-origin:0 0;background:var(--backdrop)}
.screen{position:absolute;top:229px;height:1419px;background:var(--paper);overflow:hidden}
.desktop-home{left:196px;width:487px}
.mobile-home{left:721px;width:191px}
.desktop-product{left:946px;width:573px}
.mobile-product{left:1548px;width:191px}
.abs{position:absolute}
.serif{font-family:"Source Serif 4",Georgia,serif}

/* brand */
.brand{display:flex;align-items:center;gap:3px;color:var(--blue);font-weight:400;white-space:nowrap}
.brand-dot{width:5px;height:5px;border-radius:50%;background:#d9797a}
.nav{display:flex;gap:12px;font-size:6px;color:var(--ink)}
.nav .active{text-decoration:underline}
.icon{width:9px;height:9px}
.status{font-size:5px;color:#555;display:flex;justify-content:space-between;width:100%;padding:0 14px}

/* imagery */
.ph-hero{background:linear-gradient(160deg,#5a6f86 0%,#33465c 45%,#6d5a4a 100%)}
.ph-tree{background:linear-gradient(180deg,#8fc6e6 0%,#b4daea 45%,#9fc36f 75%,#e2cf78 100%)}
.ph-bird{background:linear-gradient(180deg,#a8d7f0 0%,#dbeef6 55%,#f1dcc3 80%,#b7d486 100%)}
.ph-cover-big{background:linear-gradient(180deg,#f2c766 0%,#a8cf7a 40%,#6f9f48 70%,#e7c04e 100%)}
.ph-meadow{background:linear-gradient(180deg,#d8ebc0 0%,#9fcb6a 50%,#6c9a44 100%)}
.ph-sketch{background:#f7f7f5;border:1px solid #d8d8d8}
.ph-field{background:linear-gradient(180deg,#a9d7ee 0%,#cde6d6 45%,#d9c264 70%,#b99a3c 100%)}
.t-orange{background:linear-gradient(180deg,#f6e7cf,#e59a3e)}
.t-night{background:linear-gradient(180deg,#24354d,#5d7188)}
.t-rose{background:#f4e6e2}
.t-sketch{background:#efece3}
.t-tan{background:linear-gradient(180deg,#cda47e,#b8865c)}

/* cards */
.book-card{position:absolute;background:var(--sand)}
.book-card .cover{position:absolute;box-shadow:1px 1px 2px rgba(0,0,0,.25)}
.caption{position:absolute;font-family:"Source Serif 4",Georgia,serif;font-size:4.6px;line-height:1.35;color:var(--muted)}
.arrow-btn{position:absolute;width:28px;height:28px;border-radius:50%;background:#fff;box-shadow:0 1px 3px rgba(0,0,0,.2);display:flex;align-items:center;justify-content:center}
.section-title{position:absolute;font-family:"Source Serif 4",Georgia,serif;color:var(--ink)}
.divider{position:absolute;height:1px;background:var(--line)}
.insta{position:absolute;background:var(--blue)}
.tile{position:absolute}

/* footer */
.foot-h{font-weight:700;color:var(--ink)}
.foot-t{color:var(--ink)}
.socials{display:flex;gap:13px}
.social{width:8px;height:8px;border:1px solid var(--ink);border-radius:50%}

/* product */
.btn{position:absolute;border:1px solid #cfd6dc;font-family:"Source Serif 4",Georgia,serif;color:var(--ink);display:flex;align-items:center;justify-content:center;letter-spacing:.3px;background:#f7f7f7}
.btn.primary{background:var(--blue);color:#fff;border-color:var(--blue)}
.qty{display:flex;align-items:center;gap:6px}
.qty span.box{border:1px solid #ddd;padding:0 3px}
.spec dt{font-family:"Source Serif 4",Georgia,serif;font-weight:600;color:var(--blue-dark)}
.spec dd{font-family:"Source Serif 4",Georgia,serif;color:var(--ink);margin-bottom:6px}
.desc p{margin-bottom:8px}
</style>
</head>
<body>
<div class="stage">

<!-- ================= Desktop start page ================= -->
<section class="screen desktop-home">
  <header>
    <div class="abs brand" style="left:35px;top:32px;font-size:11px"><span>Bunte Welt</span><span class="brand-dot"></span></div>
    <nav class="abs nav" style="left:104px;top:36px"><span class="active">Start</span><span>Bücher</span><span>Verlag</span><span>Kitas/Schulen</span><span>Blog</span></nav>
    <svg class="abs icon" style="left:411px;top:34px" viewBox="0 0 10 10" fill="none" stroke="#4a6f8b"><circle cx="4" cy="4" r="3"/><path d="M6.3 6.3 9 9"/></svg>
    <svg class="abs icon" style="left:433px;top:33px" viewBox="0 0 10 10" fill="none" stroke="#4a6f8b"><rect x="1.5" y="3" width="7" height="6"/><path d="M3.5 3V2a1.5 1.5 0 0 1 3 0v1"/></svg>
  </header>

  <div class="abs" style="left:0;top:65px;width:234px;height:203px;background:var(--sand)"></div>
  <p class="abs" style="left:35px;top:73px;font-size:5px">Schön, dass du da bist!</p>
  <h1 class="abs" style="left:35px;top:96px;width:190px;font-size:19px;line-height:1.05;font-weight:500;letter-spacing:.6px;color:var(--blue-dark)">Wir sind der Seraph Verlag. Wir lieben Bücher.</h1>
  <p class="abs" style="left:35px;top:166px;width:170px;font-size:4.4px;line-height:1.7">Lorem ipsum dolor sit amet, consetetur sadipscing elitr, sed diam nonumy eirmod tempor invidunt ut labore et dolore magna aliquyam erat, sed diam voluptua. At vero eos et accusam et justo duo dolores et ea rebum. Stet clita kasd gubergren, no sea takimata sanctus est Lorem ipsum dolor sit amet</p>
  <div class="abs ph-hero" style="left:234px;top:65px;width:253px;height:203px" role="img" aria-label="Foto: zwei Kinder lesen abends gemeinsam ein Buch"></div>

  <h2 class="section-title" style="left:35px;top:292px;font-size:8px">Bilingual Books</h2>
  <div class="book-card" style="left:35px;top:318px;width:101px;height:124px"><div class="cover ph-tree" style="left:15px;top:18px;width:70px;height:88px" role="img" aria-label="Buchcover Der tanzende Berg"></div></div>
  <div class="book-card" style="left:142px;top:318px;width:101px;height:124px"><div class="cover ph-bird" style="left:6px;top:18px;width:89px;height:70px" role="img" aria-label="Buchcover Schwimm, kleiner Fisch"></div></div>
  <div class="book-card" style="left:248px;top:318px;width:101px;height:124px"><div class="cover ph-tree" style="left:15px;top:18px;width:70px;height:88px" role="img" aria-label="Buchcover Der tanzende Berg"></div></div>
  <div class="book-card" style="left:355px;top:318px;width:101px;height:124px"><div class="cover ph-bird" style="left:6px;top:18px;width:89px;height:70px" role="img" aria-label="Buchcover Schwimm, kleiner Fisch"></div></div>
  <p class="caption" style="left:35px;top:446px">Der tanzende Berg<br>The Dancing Hill<br>$11,95</p>
  <p class="caption" style="left:142px;top:446px">Schwimm, kleiner Fisch<br>Swim, Little Fish<br>$9,95</p>
  <p class="caption" style="left:248px;top:446px">Der tanzende Berg<br>The Dancing Hill<br>$11,95</p>
  <p class="caption" style="left:355px;top:446px">Schwimm, kleiner Fisch<br>Swim, Little Fish<br>$9,95</p>
  <div class="arrow-btn" style="left:21px;top:361px"><svg width="8" height="10" viewBox="0 0 8 10" fill="none" stroke="#333"><path d="M6 1 2 5l4 4"/></svg></div>
  <div class="arrow-btn" style="left:440px;top:361px"><svg width="8" height="10" viewBox="0 0 8 10" fill="none" stroke="#333"><path d="M2 1l4 4-4 4"/></svg></div>
  <div class="divider" style="left:35px;top:495px;width:422px"></div>

  <h2 class="section-title" style="left:35px;top:524px;font-size:8px">One Language Books</h2>
  <div class="book-card" style="left:35px;top:550px;width:101px;height:124px"><div class="cover ph-tree" style="left:15px;top:18px;width:70px;height:88px" role="img" aria-label="Buchcover Der tanzende Berg"></div></div>
  <div class="book-card" style="left:142px;top:550px;width:101px;height:124px"><div class="cover ph-bird" style="left:6px;top:18px;width:89px;height:70px" role="img" aria-label="Buchcover Schwimm, kleiner Fisch"></div></div>
  <div class="book-card" style="left:248px;top:550px;width:101px;height:124px"><div class="cover ph-tree" style="left:15px;top:18px;width:70px;height:88px" role="img" aria-label="Buchcover Der tanzende Berg"></div></div>
  <div class="book-card" style="left:355px;top:550px;width:101px;height:124px"><div class="cover ph-bird" style="left:6px;top:18px;width:89px;height:70px" role="img" aria-label="Buchcover Schwimm, kleiner Fisch"></div></div>
  <p class="caption" style="left:35px;top:678px">Der tanzende Berg<br>The Dancing Hill<br>$11,95</p>
  <p class="caption" style="left:142px;top:678px">Schwimm, kleiner Fisch<br>Swim, Little Fish<br>$9,95</p>
  <p class="caption" style="left:248px;top:678px">Der tanzende Berg<br>The Dancing Hill<br>$11,95</p>
  <p class="caption" style="left:355px;top:678px">Schwimm, kleiner Fisch<br>Swim, Little Fish<br>$9,95</p>
  <div class="arrow-btn" style="left:21px;top:604px"><svg width="8" height="10" viewBox="0 0 8 10" fill="none" stroke="#333"><path d="M6 1 2 5l4 4"/></svg></div>
  <div class="arrow-btn" style="left:440px;top:604px"><svg width="8" height="10" viewBox="0 0 8 10" fill="none" stroke="#333"><path d="M2 1l4 4-4 4"/></svg></div>
  <div class="divider" style="left:35px;top:732px;width:422px"></div>

  <h2 class="section-title" style="left:35px;top:761px;font-size:8px">Activity Books</h2>
  <div class="book-card" style="left:35px;top:787px;width:101px;height:124px"><div class="cover ph-tree" style="left:15px;top:18px;width:70px;height:88px" role="img" aria-label="Buchcover Der tanzende Berg"></div></div>
  <div class="book-card" style="left:142px;top:787px;width:101px;height:124px"><div class="cover ph-bird" style="left:6px;top:18px;width:89px;height:70px" role="img" aria-label="Buchcover Schwimm, kleiner Fisch"></div></div>
  <div class="book-card" style="left:248px;top:787px;width:101px;height:124px"><div class="cover ph-tree" style="left:15px;top:18px;width:70px;height:88px" role="img" aria-label="Buchcover Der tanzende Berg"></div></div>
  <div class="book-card" style="left:355px;top:787px;width:101px;height:124px"><div class="cover ph-bird" style="left:6px;top:18px;width:89px;height:70px" role="img" aria-label="Buchcover Schwimm, kleiner Fisch"></div></div>
  <p class="caption" style="left:35px;top:915px">Der tanzende Berg<br>The Dancing Hill<br>$11,95</p>
  <p class="caption" style="left:142px;top:915px">Schwimm, kleiner Fisch<br>Swim, Little Fish<br>$9,95</p>
  <p class="caption" style="left:248px;top:915px">Der tanzende Berg<br>The Dancing Hill<br>$11,95</p>
  <p class="caption" style="left:355px;top:915px">Schwimm, kleiner Fisch<br>Swim, Little Fish<br>$9,95</p>
  <div class="arrow-btn" style="left:21px;top:842px"><svg width="8" height="10" viewBox="0 0 8 10" fill="none" stroke="#333"><path d="M6 1 2 5l4 4"/></svg></div>
  <div class="arrow-btn" style="left:440px;top:842px"><svg width="8" height="10" viewBox="0 0 8 10" fill="none" stroke="#333"><path d="M2 1l4 4-4 4"/></svg></div>

  <h2 class="section-title" style="left:35px;top:979px;font-size:8px">@karlsplanet</h2>
  <div class="insta" style="left:0;top:998px;width:487px;height:192px"></div>
  <div class="tile t-orange" style="left:32px;top:1014px;width:81px;height:80px" role="img" aria-label="Social-Media-Beitrag: Buchcover"></div>
  <div class="tile t-night" style="left:118px;top:1014px;width:81px;height:80px" role="img" aria-label="Social-Media-Beitrag: Kinder bei Nacht"></div>
  <div class="tile t-rose" style="left:204px;top:1014px;width:81px;height:80px" role="img" aria-label="Social-Media-Beitrag: Vorlesen"></div>
  <div class="tile t-sketch" style="left:289px;top:1014px;width:81px;height:80px" role="img" aria-label="Social-Media-Beitrag: Malvorlage"></div>
  <div class="tile t-tan" style="left:374px;top:1014px;width:81px;height:80px" role="img" aria-label="Social-Media-Beitrag: Buch in der Hand"></div>
  <div class="tile t-night" style="left:32px;top:1098px;width:81px;height:80px" role="img" aria-label="Social-Media-Beitrag: Kinder bei Nacht"></div>
  <div class="tile t-rose" style="left:118px;top:1098px;width:81px;height:80px" role="img" aria-label="Social-Media-Beitrag: Vorlesen"></div>
  <div class="tile t-tan" style="left:204px;top:1098px;width:81px;height:80px" role="img" aria-label="Social-Media-Beitrag: Buch in der Hand"></div>
  <div class="tile t-sketch" style="left:289px;top:1098px;width:81px;height:80px" role="img" aria-label="Social-Media-Beitrag: Malvorlage"></div>
  <div class="tile t-orange" style="left:374px;top:1098px;width:81px;height:80px" role="img" aria-label="Social-Media-Beitrag: Buchcover"></div>

  <footer>
    <div class="abs" style="left:35px;top:1298px;width:160px;font-size:4.4px;line-height:1.6">
      <p class="foot-h" style="margin-bottom:8px">Kundenservice</p>
      <p class="foot-t">Du hast Fragen zu unseren Büchern oder Deiner Bestellung?<br>Meld Dich einfach bei hallo@honigtauverlag.de – wir antworten so schnell es geht.</p>
    </div>
    <div class="abs" style="left:264px;top:1298px;font-size:4.4px;line-height:2.6">
      <p class="foot-h" style="line-height:1.6;margin-bottom:5px">Kontakt</p><p>Handel</p><p>Presse</p><p>Karriere</p>
    </div>
    <div class="abs" style="left:365px;top:1298px;font-size:4.4px;line-height:2.6">
      <p class="foot-h" style="line-height:1.6;margin-bottom:5px">Kleingedrucktes</p><p>Impressum</p><p>AGB</p><p>Datenschutzerklärung</p>
    </div>
    <div class="abs socials" style="left:37px;top:1383px"><span class="social"></span><span class="social"></span><span class="social"></span></div>
    <p class="abs" style="left:0;width:100%;top:1399px;text-align:center;font-size:4.4px">© 2022, Bunte Welt Verlag</p>
  </footer>
</section>

<!-- ================= Mobile start page ================= -->
<section class="screen mobile-home">
  <div class="abs status" style="top:6px"><span>11:11</span><span>●●▮</span></div>
  <svg class="abs" style="left:16px;top:27px" width="11" height="8" viewBox="0 0 11 8" stroke="#4a6f8b"><path d="M0 1h11M0 4h11M0 7h11"/></svg>
  <div class="abs brand" style="left:62px;top:24px;font-size:10px"><span>Bunte Welt</span><span class="brand-dot"></span></div>
  <svg class="abs icon" style="left:145px;top:26px" viewBox="0 0 10 10" fill="none" stroke="#4a6f8b"><circle cx="4" cy="4" r="3"/><path d="M6.3 6.3 9 9"/></svg>
  <svg class="abs icon" style="left:161px;top:25px" viewBox="0 0 10 10" fill="none" stroke="#4a6f8b"><rect x="1.5" y="3" width="7" height="6"/><path d="M3.5 3V2a1.5 1.5 0 0 1 3 0v1"/></svg>
  <div class="abs ph-hero" style="left:0;top:54px;width:191px;height:164px" role="img" aria-label="Foto: zwei Kinder lesen abends gemeinsam ein Buch"></div>

  <p class="abs" style="left:0;width:100%;top:229px;text-align:center;font-size:6.4px">Schön, dass du da bist!</p>
  <h1 class="abs" style="left:10px;width:171px;top:247px;text-align:center;font-size:9.6px;line-height:1.3;font-weight:500;letter-spacing:.4px;color:var(--blue-dark)">Wir sind der Seraph Verlag. Wir lieben Bücher.</h1>
  <p class="abs" style="left:14px;width:163px;top:281px;text-align:center;font-size:6.2px;line-height:1.75">Lorem ipsum dolor sit amet, consetetur sadipscing elitr, sed diam nonumy eirmod tempor invidunt ut labore et dolore magna aliquyam erat, sed diam voluptua. At vero eos et accusam et justo duo dolores et ea rebum. Stet clita kasd gubergren, no sea takimata sanctus est Lorem ipsum dolor sit amet</p>

  <h2 class="section-title" style="left:0;width:100%;text-align:center;top:412px;font-size:7.6px">Bilingual Books</h2>
  <div class="book-card" style="left:15px;top:440px;width:78px;height:106px"><div class="cover ph-bird" style="left:5px;top:8px;width:68px;height:62px" role="img" aria-label="Buchcover Schwimm, kleiner Fisch"></div><p class="caption" style="left:5px;top:75px;font-size:4px">Schwimm, kleiner Fisch<br>Swim, Little Fish<br><span style="font-size:6px">$9,95</span></p></div>
  <div class="book-card" style="left:98px;top:440px;width:78px;height:106px"><div class="cover ph-tree" style="left:12px;top:6px;width:54px;height:66px" role="img" aria-label="Buchcover Der tanzende Berg"></div><p class="caption" style="left:5px;top:75px;font-size:4px">Der tanzende Berg<br>The Dancing Hill<br><span style="font-size:6px">$11,95</span></p></div>

  <h2 class="section-title" style="left:0;width:100%;text-align:center;top:567px;font-size:7.6px">One Language Books</h2>
  <div class="book-card" style="left:15px;top:595px;width:78px;height:106px"><div class="cover ph-bird" style="left:5px;top:8px;width:68px;height:62px" role="img" aria-label="Buchcover Schwimm, kleiner Fisch"></div><p class="caption" style="left:5px;top:75px;font-size:4px">Schwimm, kleiner Fisch<br>Swim, Little Fish<br><span style="font-size:6px">$9,95</span></p></div>
  <div class="book-card" style="left:98px;top:595px;width:78px;height:106px"><div class="cover ph-tree" style="left:12px;top:6px;width:54px;height:66px" role="img" aria-label="Buchcover Der tanzende Berg"></div><p class="caption" style="left:5px;top:75px;font-size:4px">Der tanzende Berg<br>The Dancing Hill<br><span style="font-size:6px">$11,95</span></p></div>

  <h2 class="section-title" style="left:0;width:100%;text-align:center;top:722px;font-size:7.6px">Activity Books</h2>
  <div class="book-card" style="left:15px;top:750px;width:78px;height:106px"><div class="cover ph-bird" style="left:5px;top:8px;width:68px;height:62px" role="img" aria-label="Buchcover Schwimm, kleiner Fisch"></div><p class="caption" style="left:5px;top:75px;font-size:4px">Schwimm, kleiner Fisch<br>Swim, Little Fish<br><span style="font-size:6px">$9,95</span></p></div>
  <div class="book-card" style="left:98px;top:750px;width:78px;height:106px"><div class="cover ph-tree" style="left:12px;top:6px;width:54px;height:66px" role="img" aria-label="Buchcover Der tanzende Berg"></div><p class="caption" style="left:5px;top:75px;font-size:4px">Der tanzende Berg<br>The Dancing Hill<br><span style="font-size:6px">$11,95</span></p></div>

  <h2 class="section-title" style="left:0;width:100%;text-align:center;top:877px;font-size:7.6px">@karlsplanet</h2>
  <div class="insta" style="left:0;top:899px;width:191px;height:141px"></div>
  <div class="tile t-orange" style="left:7px;top:913px;width:57px;height:55px" role="img" aria-label="Social-Media-Beitrag: Buchcover"></div>
  <div class="tile t-night" style="left:67px;top:913px;width:57px;height:55px" role="img" aria-label="Social-Media-Beitrag: Kinder bei Nacht"></div>
  <div class="tile t-rose" style="left:127px;top:913px;width:57px;height:55px" role="img" aria-label="Social-Media-Beitrag: Vorlesen"></div>
  <div class="tile t-night" style="left:7px;top:972px;width:57px;height:55px" role="img" aria-label="Social-Media-Beitrag: Kinder bei Nacht"></div>
  <div class="tile t-rose" style="left:67px;top:972px;width:57px;height:55px" role="img" aria-label="Social-Media-Beitrag: Vorlesen"></div>
  <div class="tile t-tan" style="left:127px;top:972px;width:57px;height:55px" role="img" aria-label="Social-Media-Beitrag: Buch in der Hand"></div>

  <footer class="abs" style="left:10px;top:1073px;width:170px;font-size:6.2px;line-height:1.75">
    <p class="foot-h">Kundenservice</p>
    <p class="foot-t">Du hast Fragen zu unseren Büchern oder Deiner Bestellung?<br>Meld Dich einfach bei hallo@honigtauverlag.de – wir antworten so schnell es geht.</p>
    <p class="foot-h" style="margin-top:12px">Kontakt</p>
    <p style="line-height:3.9">Handel<br>Presse<br>Karriere</p>
    <p class="foot-h" style="margin-top:2px">Kleingedrucktes</p>
    <p style="line-height:3.9">Impressum<br>AGB<br>Datenschutzerklärung</p>
    <div class="socials" style="margin-top:8px"><span class="social"></span><span class="social"></span><span class="social"></span></div>
    <p style="text-align:center;margin-top:14px">© 2022, Bunte Welt Verlag</p>
  </footer>
</section>

<!-- ================= Desktop product page ================= -->
<section class="screen desktop-product">
  <div class="abs brand" style="left:40px;top:40px;font-size:12px"><span>Bunte Welt</span><span class="brand-dot"></span></div>
  <nav class="abs nav" style="left:122px;top:43px;font-size:6.4px;gap:14px"><span class="active">Start</span><span>Bücher</span><span>Verlag</span><span>Kitas/Schulen</span><span>Blog</span></nav>
  <svg class="abs icon" style="left:485px;top:40px" viewBox="0 0 10 10" fill="none" stroke="#4a6f8b"><circle cx="4" cy="4" r="3"/><path d="M6.3 6.3 9 9"/></svg>
  <svg class="abs icon" style="left:511px;top:39px" viewBox="0 0 10 10" fill="none" stroke="#4a6f8b"><rect x="1.5" y="3" width="7" height="6"/><path d="M3.5 3V2a1.5 1.5 0 0 1 3 0v1"/></svg>
  <p class="abs" style="left:41px;top:75px;font-size:5.4px;line-height:1.5">Home / BILINGUAL BOOKS-HOME /<br><span style="color:#3f78a8">The Dancing Hill - La Colline Dansante (English/French)</span></p>

  <div class="abs" style="left:41px;top:106px;width:253px;height:648px;background:var(--sand)"></div>
  <div class="abs ph-cover-big" style="left:90px;top:126px;width:151px;height:196px;box-shadow:1px 1px 3px rgba(0,0,0,.25)" role="img" aria-label="Buchcover The Dancing Hill"></div>
  <div class="abs ph-meadow" style="left:90px;top:331px;width:151px;height:151px" role="img" aria-label="Innenseite: Berg auf einer Wiese mit Tieren"></div>
  <div class="abs ph-sketch" style="left:90px;top:489px;width:73px;height:73px" role="img" aria-label="Ausmalseite mit Figur"></div>
  <div class="abs ph-sketch" style="left:168px;top:489px;width:73px;height:73px" role="img" aria-label="Ausmalseite mit Landschaft"></div>
  <div class="abs ph-field" style="left:90px;top:571px;width:151px;height:151px" role="img" aria-label="Innenseite: Feld mit Traktor unter blauem Himmel"></div>

  <div class="abs" style="left:309px;top:106px;width:215px">
    <p style="font-size:5.6px">KARL WENDT</p>
    <h1 class="serif" style="font-size:13px;line-height:1.45;font-weight:400;letter-spacing:.4px;margin-top:6px;color:var(--blue-dark)">The Dancing Hill - La Colline Dansante (English/French)</h1>
    <p class="serif" style="font-size:10px;margin-top:7px">$12.95</p>
    <p class="serif" style="font-size:5px;font-style:italic;margin-top:3px">inkl. MwSt. und Versand</p>
    <div class="qty" style="font-size:5px;margin-top:11px"><span>Anzahl</span><span class="box">-</span><span>1</span><span class="box">+</span></div>
  </div>
  <div class="btn" style="left:309px;top:231px;width:168px;height:19px;font-size:5.6px">E-BOOK</div>
  <div class="btn primary" style="left:309px;top:258px;width:168px;height:19px;font-size:5.6px">PAPERBACK</div>

  <div class="abs desc" style="left:310px;top:289px;width:210px;font-size:5.4px;line-height:1.45">
    <p>A Vivid Story About the Importance of Home and The Place We Love the Most.<br>"In a valley, there stood a hill. He felt lonely and bored and wanted to move away. "I wish I could dance across the land and see the world from above— from this place, I want to go."</p>
    <p>When a cheerful swallow helps him to lift his roots and dance, he finds himself far away, looking back at the valley. What will he see? And finally: Will he dance back home where he belongs?</p>
    <p>Kids will learn different places, objects, and simple questions and answers.</p>
    <p>Here's what makes this book special:</p>
    <p>Each sentence is both in English and French<br>The story is simple and suitable for early age learning<br>All the illustrations are original, creative, and fun<br>EXTRA PAGES for coloring</p>
    <p>Kids learn quickly and easily. With bilingual children's books, you set them up for success and expand their horizons from an early age! This dual language book is part of a series of bedtime stories that are specifically designed to teach children new foreign words and phrases as you read to them.</p>
    <p>Teach Your Children First Words in English or French.</p>
  </div>
  <dl class="abs spec" style="left:310px;top:573px;width:210px;font-size:5.4px;line-height:1.45">
    <dt>Buchtitel</dt><dd>The Dancing Hill - La Colline Dansante (English/French)</dd>
    <dt>Dateigröße</dt><dd>60 pages</dd>
    <dt>Autor</dt><dd>Karl Wendt</dd>
    <dt>ISBN</dt><dd>979-8123456789</dd>
    <dt>Edition Sprache</dt><dd>English, French</dd>
    <dt>Buchformat</dt><dd>8.5 x 11</dd>
    <dt>Veröffentlichungsdatum</dt><dd>October 29, 2021</dd>
  </dl>

  <h2 class="section-title" style="left:41px;top:823px;font-size:8.6px">Related Products</h2>
  <div class="book-card" style="left:38px;top:852px;width:119px;height:146px"><div class="cover ph-tree" style="left:22px;top:23px;width:75px;height:95px" role="img" aria-label="Buchcover Der tanzende Berg"></div></div>
  <div class="book-card" style="left:164px;top:852px;width:119px;height:146px"><div class="cover ph-bird" style="left:8px;top:23px;width:103px;height:80px" role="img" aria-label="Buchcover Schwimm, kleiner Fisch"></div></div>
  <div class="book-card" style="left:290px;top:852px;width:119px;height:146px"><div class="cover ph-tree" style="left:22px;top:23px;width:75px;height:95px" role="img" aria-label="Buchcover Der tanzende Berg"></div></div>
  <div class="book-card" style="left:416px;top:852px;width:119px;height:146px"><div class="cover ph-bird" style="left:8px;top:23px;width:103px;height:80px" role="img" aria-label="Buchcover Schwimm, kleiner Fisch"></div></div>
  <p class="caption" style="left:38px;top:1003px;font-size:5.4px">Der tanzende Berg<br>The Dancing Hill<br>$11,95</p>
  <p class="caption" style="left:164px;top:1003px;font-size:5.4px">Schwimm, kleiner Fisch<br>Swim, Little Fish<br>$9,95</p>
  <p class="caption" style="left:290px;top:1003px;font-size:5.4px">Der tanzende Berg<br>The Dancing Hill<br>$11,95</p>
  <p class="caption" style="left:416px;top:1003px;font-size:5.4px">Schwimm, kleiner Fisch<br>Swim, Little Fish<br>$9,95</p>

  <footer>
    <div class="abs" style="left:42px;top:1268px;width:190px;font-size:5px;line-height:1.6">
      <p class="foot-h" style="margin-bottom:10px">Kundenservice</p>
      <p class="foot-t">Du hast Fragen zu unseren Büchern oder Deiner Bestellung?<br>Meld Dich einfach bei hallo@honigtauverlag.de – wir antworten so schnell es geht.</p>
    </div>
    <div class="abs" style="left:311px;top:1268px;font-size:5px;line-height:3">
      <p class="foot-h" style="line-height:1.6;margin-bottom:6px">Kontakt</p><p>Handel</p><p>Presse</p><p>Karriere</p>
    </div>
    <div class="abs" style="left:430px;top:1268px;font-size:5px;line-height:3">
      <p class="foot-h" style="line-height:1.6;margin-bottom:6px">Kleingedrucktes</p><p>Impressum</p><p>AGB</p><p>Datenschutzerklärung</p>
    </div>
    <div class="abs socials" style="left:44px;top:1368px;gap:17px"><span class="social"></span><span class="social"></span><span class="social"></span></div>
    <p class="abs" style="left:0;width:100%;top:1386px;text-align:center;font-size:5px">© 2022, Bunte Welt Verlag</p>
  </footer>
</section>

<!-- ================= Mobile product page ================= -->
<section class="screen mobile-product">
  <div class="abs status" style="top:6px"><span>11:11</span><span>●●▮</span></div>
  <svg class="abs" style="left:16px;top:27px" width="11" height="8" viewBox="0 0 11 8" stroke="#4a6f8b"><path d="M0 1h11M0 4h11M0 7h11"/></svg>
  <div class="abs brand" style="left:62px;top:24px;font-size:10px"><span>Bunte Welt</span><span class="brand-dot"></span></div>
  <svg class="abs icon" style="left:145px;top:26px" viewBox="0 0 10 10" fill="none" stroke="#4a6f8b"><circle cx="4" cy="4" r="3"/><path d="M6.3 6.3 9 9"/></svg>
  <svg class="abs icon" style="left:161px;top:25px" viewBox="0 0 10 10" fill="none" stroke="#4a6f8b"><rect x="1.5" y="3" width="7" height="6"/><path d="M3.5 3V2a1.5 1.5 0 0 1 3 0v1"/></svg>

  <div class="abs" style="left:0;top:54px;width:191px;height:214px;background:var(--sand)"></div>
  <div class="abs ph-cover-big" style="left:28px;top:70px;width:134px;height:172px;box-shadow:1px 1px 3px rgba(0,0,0,.25)" role="img" aria-label="Buchcover The Dancing Hill"></div>
  <svg class="abs" style="left:10px;top:144px" width="8" height="14" viewBox="0 0 8 14" fill="none" stroke="#fff" stroke-width="1.5"><path d="M7 1 1 7l6 6"/></svg>
  <svg class="abs" style="left:172px;top:144px" width="8" height="14" viewBox="0 0 8 14" fill="none" stroke="#fff" stroke-width="1.5"><path d="M1 1l6 6-6 6"/></svg>

  <div class="abs" style="left:14px;top:277px;width:165px">
    <p style="font-size:5px">KARL WENDT</p>
    <h1 style="font-size:6.6px;line-height:1.4;font-weight:400;margin-top:4px;color:var(--blue-dark)">The Dancing Hill - La Colline Dansante (English/French)</h1>
    <p class="serif" style="font-size:6.4px;margin-top:6px">$12.95</p>
    <p class="serif" style="font-size:4.6px;font-style:italic;margin-top:1px">inkl. MwSt. und Versand</p>
    <div class="qty" style="font-size:4.6px;margin-top:13px"><span>Anzahl</span><span class="box">-</span><span>1</span><span class="box">+</span></div>
  </div>
  <div class="btn" style="left:14px;top:384px;width:159px;height:17px;font-size:5.4px">E-BOOK</div>
  <div class="btn primary" style="left:14px;top:410px;width:159px;height:18px;font-size:5.4px">PAPERBACK</div>

  <div class="abs desc" style="left:14px;top:446px;width:160px;font-size:4.5px;line-height:1.5">
    <p>A Vivid Story About the Importance of Home and The Place We Love the Most.<br>"In a valley, there stood a hill. He felt lonely and bored and wanted to move away. "I wish I could dance across the land and see the world from above— from this place, I want to go."</p>
    <p>When a cheerful swallow helps him to lift his roots and dance, he finds himself far away, looking back at the valley. What will he see? And finally: Will he dance back home where he belongs?</p>
    <p>Kids will learn different places, objects, and simple questions and answers.</p>
    <p>Here's what makes this book special:</p>
    <p>Each sentence is both in English and French<br>The story is simple and suitable for early age learning<br>All the illustrations are original, creative, and fun<br>EXTRA PAGES for coloring</p>
    <p>Kids learn quickly and easily. With bilingual children's books, you set them up for success and expand their horizons from an early age! This dual language book is part of a series of bedtime stories that are specifically designed to teach children new foreign words and phrases as you read to them.</p>
    <p>Teach Your Children First Words in English or French.</p>
  </div>
  <dl class="abs spec" style="left:14px;top:720px;width:160px;font-size:4.5px;line-height:1.5">
    <dt>Buchtitel</dt><dd>The Dancing Hill - La Colline Dansante (English/French)</dd>
    <dt>Dateigröße</dt><dd>60 pages</dd>
    <dt>Autor</dt><dd>Karl Wendt</dd>
    <dt>ISBN</dt><dd>979-8123456789</dd>
    <dt>Edition Sprache</dt><dd>English, French</dd>
    <dt>Buchformat</dt><dd>8.5 x 11</dd>
    <dt>Veröffentlichungsdatum</dt><dd>October 29, 2021</dd>
  </dl>

  <h2 class="section-title" style="left:0;width:100%;text-align:center;top:905px;font-size:7.6px">Related Products</h2>
  <div class="book-card" style="left:15px;top:929px;width:78px;height:106px"><div class="cover ph-bird" style="left:5px;top:8px;width:68px;height:62px" role="img" aria-label="Buchcover Schwimm, kleiner Fisch"></div><p class="caption" style="left:5px;top:75px;font-size:4px">Schwimm, kleiner Fisch<br>Swim, Little Fish<br><span style="font-size:6px">$9,95</span></p></div>
  <div class="book-card" style="left:98px;top:929px;width:78px;height:106px"><div class="cover ph-tree" style="left:12px;top:6px;width:54px;height:66px" role="img" aria-label="Buchcover Der tanzende Berg"></div><p class="caption" style="left:5px;top:75px;font-size:4px">Der tanzende Berg<br>The Dancing Hill<br><span style="font-size:6px">$11,95</span></p></div>

  <footer class="abs" style="left:10px;top:1073px;width:170px;font-size:6.2px;line-height:1.75">
    <p class="foot-h">Kundenservice</p>
    <p class="foot-t">Du hast Fragen zu unseren Büchern oder Deiner Bestellung?<br>Meld Dich einfach bei hallo@honigtauverlag.de – wir antworten so schnell es geht.</p>
    <p class="foot-h" style="margin-top:12px">Kontakt</p>
    <p style="line-height:3.9">Handel<br>Presse<br>Karriere</p>
    <p class="foot-h" style="margin-top:2px">Kleingedrucktes</p>
    <p style="line-height:3.9">Impressum<br>AGB<br>Datenschutzerklärung</p>
    <div class="socials" style="margin-top:8px"><span class="social"></span><span class="social"></span><span class="social"></span></div>
    <p style="text-align:center;margin-top:14px">© 2022, Bunte Welt Verlag</p>
  </footer>
</section>

</div>
</body>
</html>
```